dorvibanks pools folder design

I need a folder similar to quillset landscaping with dorvibanks pool, maybe have blue water in background or something around those lines. same quote in front and lay out in back. phone numbers etc. pictures in back to be e frame of some sort i understand additional monies will be paid for this

```html
<!DOCTYPE html>
<html lang="en">
<head>
<meta charset="utf-8">
<title>Dorvibanks Pools – Folder</title>
<link href="https://fonts.googleapis.com/css2?family=Fjalla+One&family=Roboto:wght@500&display=swap" rel="stylesheet">
<style>
  :root {
    --backdrop: #c4c4c4;
    --navy-deep: #0c2a5c;
    --navy: #123f86;
    --navy-light: #1d5cb0;
    --gold: #fbb21b;
    --sky: #6fb3e6;
    --white: #ffffff;
    --badge-text: #163f7e;
  }
  html, body {
    margin: 0;
    padding: 0;
    width: 1051px;
    height: 1200px;
    overflow: hidden;
    background: var(--backdrop);
  }
  .folder-dieline {
    position: absolute;
    left: 28px;
    top: 162px;
    width: 995px;
    height: 876px;
    display: block;
  }
  .tagline, .contact-heading, .badge-name {
    font-family: "Fjalla One", "Arial Narrow", sans-serif;
  }
  .contact-detail {
    font-family: "Roboto", Arial, sans-serif;
    font-weight: 500;
  }
</style>
</head>
<body>
<svg class="folder-dieline" viewBox="0 0 995 876" xmlns="http://www.w3.org/2000/svg">
  <defs>
    <linearGradient id="coverBlue" x1="0" y1="0" x2="0" y2="1">
      <stop offset="0" stop-color="var(--navy)"/>
      <stop offset="1" stop-color="var(--navy-deep)"/>
    </linearGradient>
    <linearGradient id="backPhotoTone" x1="0" y1="0" x2="0" y2="1">
      <stop offset="0" stop-color="#1a4c8e"/>
      <stop offset="0.55" stop-color="#123b72"/>
      <stop offset="1" stop-color="#0e3266"/>
    </linearGradient>
    <linearGradient id="poolSceneTone" x1="0" y1="0" x2="0" y2="1">
      <stop offset="0" stop-color="#3f7a4e"/>
      <stop offset="0.35" stop-color="#4f8fbf"/>
      <stop offset="0.7" stop-color="#1f5fc4"/>
      <stop offset="1" stop-color="#c9b79a"/>
    </linearGradient>
    <radialGradient id="swimmerTone" cx="0.5" cy="0.5" r="0.6">
      <stop offset="0" stop-color="#7fc6de"/>
      <stop offset="1" stop-color="#2f8fb8"/>
    </radialGradient>
    <radialGradient id="childTone" cx="0.5" cy="0.5" r="0.6">
      <stop offset="0" stop-color="#a6e04a"/>
      <stop offset="1" stop-color="#2a8fc0"/>
    </radialGradient>
  </defs>

  <!-- Cover spread background -->
  <rect class="cover-base" x="0" y="0" width="995" height="692" fill="url(#coverBlue)"/>

  <!-- Back panel faded pool backdrop -->
  <g role="img" aria-label="Faded photo of a pool at dusk with palm trees">
    <rect x="0" y="0" width="497" height="692" fill="url(#backPhotoTone)" opacity="0.85"/>
  </g>

  <!-- Gold sweep -->
  <path class="gold-sweep" d="M284 0 C296 250 410 410 560 448 C700 484 880 456 995 366" fill="none" stroke="var(--gold)" stroke-width="16"/>

  <!-- Front pool photo -->
  <g role="img" aria-label="Photo of a resort infinity pool with palm trees, umbrellas and blue loungers">
    <path d="M304 0 L995 0 L995 340 C880 432 700 462 562 424 C432 388 318 250 304 0 Z" fill="url(#poolSceneTone)"/>
  </g>

  <!-- Inset photo circles -->
  <g class="inset-photo">
    <circle cx="305" cy="162" r="93" fill="var(--navy-light)"/>
    <g role="img" aria-label="Photo of a woman exercising with water weights in a pool">
      <circle cx="305" cy="162" r="84" fill="url(#swimmerTone)"/>
    </g>
  </g>
  <g class="inset-photo">
    <circle cx="396" cy="351" r="97" fill="var(--navy-light)"/>
    <g role="img" aria-label="Photo of a child in sunglasses floating on a green ring">
      <circle cx="396" cy="351" r="88" fill="url(#childTone)"/>
    </g>
  </g>

  <!-- Front name badge -->
  <g class="name-badge">
    <polygon points="680,430 834,430 870,487 834,544 680,544 644,487" fill="var(--white)" stroke="var(--sky)" stroke-width="5"/>
    <text class="badge-name" x="757" y="496" text-anchor="middle" font-size="26" fill="var(--badge-text)">Dorvibanks Pools</text>
  </g>

  <!-- Front tagline -->
  <text class="tagline" x="746" y="606" text-anchor="middle" font-size="29" fill="var(--white)">We focus on making your pool safe</text>
  <text class="tagline" x="746" y="642" text-anchor="middle" font-size="29" fill="var(--white)">you can focus on it</text>

  <!-- Back panel contact block -->
  <text class="contact-heading" x="55" y="622" font-size="34" fill="var(--white)">CONTACT US</text>
  <g class="contact-phone">
    <circle cx="62" cy="643" r="6" fill="var(--white)"/>
    <path d="M59 639 q0 6 6 8" stroke="var(--navy)" stroke-width="1.8" fill="none"/>
    <text class="contact-detail" x="75" y="649" font-size="17" fill="var(--white)">(555) 018 2746</text>
  </g>
  <g class="contact-web">
    <circle cx="62" cy="664" r="5.5" fill="none" stroke="var(--white)" stroke-width="1.4"/>
    <line x1="56.5" y1="664" x2="67.5" y2="664" stroke="var(--white)" stroke-width="1.2"/>
    <ellipse cx="62" cy="664" rx="2.4" ry="5.5" fill="none" stroke="var(--white)" stroke-width="1.2"/>
    <text class="contact-detail" x="75" y="670" font-size="16" fill="var(--white)">www.dorvibankspools.com</text>
  </g>

  <!-- Back name badge -->
  <g class="name-badge name-badge--small">
    <polygon points="306,590 402,590 428,627 402,664 306,664 280,627" fill="var(--white)" stroke="var(--sky)" stroke-width="4"/>
    <text class="badge-name" x="354" y="634" text-anchor="middle" font-size="17" fill="var(--badge-text)">Dorvibanks Pools</text>
  </g>

  <!-- Pocket -->
  <polygon class="pocket" points="0,692 995,692 995,876 525,876 494,710 469,876 0,876" fill="var(--gold)"/>
</svg>
</body>
</html>
```